Luxury Toilet Rental Business. Wavelet Hire.

Wavelet Hire (the logo is in the uploaded files)
We RENT and SELL Luxury Trailer toilets.
- Show location, number, pricing, pictures.
- We have two stall trailers for rent AND 3 stall trailers
- We sell them too
- We want our phone number shown
- We are a local company
- Slogan: Elevate your event with Wavelet Hire. The Luxurious Loo
- We want a pricing portion
- We want the sizes shown
- We want the different rates/ prices shown
- We do 1 day rentals
- We do 1 week rentals
- We want the service area. We serve Los Angeles County, Orange County, Riverside County, San Bernardino County, and Palm Desert.
- Our location is in Santa Ana California

Target Market(s)

Event planners, wedding planners, venue planners, concerts, events, gatherings.

Industry/Entity Type

Luxury Toilet Rentals

Number of Pages Required

1 page

Font styles to use
Serif
Sans Serif

Colors
EE7325
F08F49
F5BC92
FAE3D3
FDF4ED

Requirements
Must have
• Location, pricing, pictures, available areas. Our slogan.
Nice to have
• I like the idea of having tabs that show price, a tab that shows our contact information, pictures, event ideas, and where we service (the areas we'll go to)

```html
<!DOCTYPE html>
<html lang="en">
<head>
<meta charset="utf-8">
<title>Wavelet Hire — Luxury Restroom Trailers</title>
<link rel="stylesheet" href="https://fonts.googleapis.com/css2?family=Poppins:wght@400;500;600;700;800&display=swap">
<style>
:root{
  --orange:#EE7325;
  --orange-2:#F08F49;
  --peach:#F5BC92;
  --cream:#FAE3D3;
  --ivory:#FDF4ED;
  --ink:#1d1d1d;
  --text:#333;
  --muted:#7a7a7a;
  --soft-bg:#f3f3f3;
  --black:#0d0d0d;
}
*{box-sizing:border-box;margin:0;padding:0}
html,body{width:1200px;height:4097px;overflow:hidden}
body{font-family:"Poppins",sans-serif;color:var(--text);background:#fff;position:relative}
svg{display:block}

/* top bar */
.topbar{position:absolute;left:0;top:0;width:1200px;height:42px;background:var(--orange);color:#fff;font-size:17px;font-weight:500}
.topbar .item{position:absolute;top:9px;display:flex;align-items:center;gap:12px}
.topbar .social{position:absolute;right:40px;top:12px;display:flex;gap:22px}
.dot{width:16px;height:16px;border-radius:50%;background:#fff;display:block}

/* nav */
.nav{position:absolute;top:42px;left:0;width:1200px;height:96px;background:#fff}
.brand{position:absolute;left:37px;top:22px;display:flex;align-items:center;gap:10px;font-size:34px;font-weight:700;color:var(--orange);letter-spacing:.5px}
.brand .sq{width:20px;height:20px;background:var(--orange)}
.menu{position:absolute;top:40px;font-size:16px;color:#444;font-weight:400}
.btn-dark{position:absolute;right:28px;top:32px;width:147px;height:36px;background:#111;color:#fff;font-size:14px;display:flex;align-items:center;justify-content:center}

/* hero */
.hero{position:absolute;top:138px;left:0;width:1200px;height:543px;background:linear-gradient(100deg,#3c4a3a 0%,#556655 35%,#2c2f30 55%,#1e2022 75%,#47513f 100%)}
.hero::after{content:"";position:absolute;inset:0;background:rgba(0,0,0,.28)}
.hero h1{position:absolute;left:45px;top:124px;z-index:2;font-size:43px;line-height:51px;font-weight:800;color:#fff;text-transform:uppercase}
.hero .btns{position:absolute;left:52px;top:365px;z-index:2;display:flex;gap:16px}
.btn{height:33px;padding:0 34px;display:flex;align-items:center;justify-content:center;font-size:15px;color:#fff;text-transform:uppercase}
.btn.orange{background:var(--orange)}
.btn.black{background:#111;padding:0 18px}

/* features */
.soft{position:absolute;left:0;top:681px;width:1200px;height:688px;background:var(--soft-bg)}
.features{position:absolute;left:148px;top:640px;width:939px;height:169px;background:#fff;border-bottom:4px solid var(--orange);box-shadow:0 2px 14px rgba(0,0,0,.08);display:flex;padding:48px 0 0 40px;gap:36px;z-index:3}
.feature{display:flex;gap:12px;width:270px}
.feature h3{font-size:24px;font-weight:500;color:#111;line-height:28px}
.feature p{font-size:9.5px;color:#888;line-height:15px;margin-top:3px}

/* about */
.about-img{position:absolute;left:52px;top:896px;width:491px;height:381px;background:linear-gradient(180deg,#8a9aa8 0%,#6d6f72 35%,#5e6163 70%,#2f8fc4 85%,#2a2a2a 100%)}
.about h2{position:absolute;left:590px;top:895px;font-size:37px;font-weight:600;color:#111}
.about .copy{position:absolute;left:594px;top:973px;width:560px;font-size:13.5px;line-height:23.4px;color:#777}
.about .copy p{margin-bottom:10px}
.about .btn{position:absolute;left:590px;top:1245px;height:32px}

/* section titles */
.title{position:absolute;left:0;width:1200px;text-align:center;font-size:37px;font-weight:600;color:#222}
.rule{position:absolute;left:50%;width:152px;height:3px;margin-left:-76px;background:var(--orange)}

/* trailers */
.cards{position:absolute;left:134px;top:1538px;display:flex}
.trailer{position:relative;width:304px;height:417px;background:linear-gradient(180deg,#7d8a94 0%,#6b6d70 40%,#4e5153 70%,#2d2f31 100%);color:#fff}
.trailer h4{position:absolute;left:26px;top:290px;font-size:22px;font-weight:600}
.trailer .spec{position:absolute;left:26px;top:335px;font-size:13px;display:flex;gap:40px}
.trailer .spec b{font-weight:600}
.trailer .spec span{color:#ddd}
.trailer .req{position:absolute;left:26px;top:373px;height:32px;padding:0 22px;background:#111;display:flex;align-items:center;font-size:14px}
.arrow{position:absolute;width:64px;height:64px}

/* events */
.events{position:absolute;top:2025px;left:0;width:1200px;height:551px;background:linear-gradient(180deg,#d9dad8 0%,#cfd1cc 50%,#c7c9c3 100%)}
.event{position:absolute;width:191px;text-align:center}
.event .pic{width:191px;height:191px;border-radius:50%}
.event span{position:absolute;left:-60px;width:311px;font-size:21px;font-weight:500;color:#111}

/* pricing */
.price-panel{position:absolute;left:99px;top:2719px;width:1018px;height:564px;background:#f2f2f2}
.price-tabbar{position:absolute;left:20px;top:12px;width:978px;height:72px;background:#ebebeb;border-radius:6px}
.plan{position:absolute;top:2815px;width:281px;height:426px;background:#fff;box-shadow:0 2px 10px rgba(0,0,0,.06);text-align:center;overflow:hidden}
.plan h5{margin-top:28px;font-size:15px;font-weight:600;color:#111}
.plan .sub{font-size:11px;color:#888;margin-top:6px}
.plan .amount{margin-top:14px;display:flex;justify-content:center;align-items:flex-end;gap:3px;color:var(--orange)}
.plan .amount small{font-size:9px;color:#333;align-self:flex-start;margin-top:6px}
.plan .amount strong{font-size:44px;font-weight:600;line-height:46px}
.plan .amount em{font-style:normal;font-size:7px;color:#555;margin-bottom:8px}
.plan ul{list-style:none;margin:24px 20px 0}
.plan li{display:flex;justify-content:space-between;align-items:center;height:35px;border-bottom:1px solid #eee;font-size:9.5px;color:#888}
.plan .choose{margin:38px auto 0;width:124px;height:37px;border:1px solid #222;font-size:10px;font-weight:600;color:#111;display:flex;align-items:center;justify-content:center}
.ribbon{position:absolute;left:-34px;top:14px;width:120px;height:22px;background:var(--orange);color:#fff;font-size:8px;line-height:22px;transform:rotate(-45deg)}

/* areas */
.area{position:absolute;display:flex;align-items:center;gap:24px;font-size:26px;font-weight:500;color:#111}
.tick{width:50px;height:50px;background:var(--orange);display:flex;align-items:center;justify-content:center}

/* footer */
.footer{position:absolute;left:0;top:3748px;width:1200px;height:349px;background:var(--black);color:#fff}
.footer .brand{left:58px;top:68px;font-size:32px}
.footer .about-text{position:absolute;left:58px;top:160px;width:300px;font-size:10.5px;line-height:18px;color:#ddd}
.footer h6{position:absolute;top:62px;font-size:18px;font-weight:600;color:var(--orange)}
.flist{position:absolute;list-style:none;font-size:16px;font-weight:500}
.flist li{display:flex;align-items:center;gap:12px;height:38px}
.fcheck{width:20px;height:20px;background:var(--orange);display:flex;align-items:center;justify-content:center}
.input{position:absolute;left:921px;top:103px;width:207px;height:36px;background:#fff;color:#999;font-size:15px;padding:6px 13px}
.signup{position:absolute;left:921px;top:149px;width:207px;height:36px;background:var(--orange);font-size:15px;display:flex;align-items:center;justify-content:center}
.footer .line{position:absolute;left:70px;top:295px;width:1060px;height:1px;background:#555}
.footer .copyright{position:absolute;left:70px;top:316px;font-size:14px;color:#ddd}
.footer .social{position:absolute;right:70px;top:313px;display:flex;gap:26px}
</style>
</head>
<body>

<header class="topbar">
  <div class="item" style="left:36px">
    <svg width="18" height="14" viewBox="0 0 18 14"><rect x="1" y="1" width="16" height="12" rx="1.5" fill="#fff"/><path d="M1.5 2 9 8l7.5-6" stroke="#EE7325" stroke-width="1.6" fill="none"/></svg>
    info@website
  </div>
  <div class="item" style="left:282px">
    <svg width="16" height="16" viewBox="0 0 24 24"><path d="M6.6 10.8a15.2 15.2 0 0 0 6.6 6.6l2.2-2.2c.3-.3.7-.4 1-.2 1.1.4 2.3.6 3.6.6.6 0 1 .4 1 1V20c0 .6-.4 1-1 1A17 17 0 0 1 3 4c0-.6.4-1 1-1h3.5c.6 0 1 .4 1 1 0 1.3.2 2.5.6 3.6.1.3 0 .7-.2 1z" fill="#fff"/></svg>
    123-456-7890
  </div>
  <div class="social"><i class="dot"></i><i class="dot"></i><i class="dot"></i></div>
</header>

<nav class="nav">
  <div class="brand"><span class="sq"></span>Wavelet Hire</div>
  <span class="menu" style="left:419px">HOME</span>
  <span class="menu" style="left:507px">ABOUT</span>
  <span class="menu" style="left:607px;top:38px">PRICES</span>
  <span class="menu" style="left:716px">LOCATIONS</span>
  <span class="menu" style="left:856px">EVENTS</span>
  <div class="btn-dark">CONTACT US</div>
</nav>

<section class="hero" role="img" aria-label="Photo of a luxury restroom trailer parked on grass beside a lake">
  <h1>Elevate your<br>event with<br>Wavelet Hire.<br>The luxurious loo</h1>
  <div class="btns"><span class="btn orange">Learn more</span><span class="btn black">Request a quote</span></div>
</section>

<div class="soft"></div>

<section class="features">
  <div class="feature">
    <svg width="72" height="72" viewBox="0 0 72 72" fill="none" stroke="#EE7325" stroke-width="2.4"><rect x="6" y="6" width="60" height="58" rx="4"/><rect x="16" y="16" width="18" height="42"/><rect x="38" y="16" width="18" height="42"/><circle cx="25" cy="30" r="3"/><circle cx="47" cy="30" r="3"/><path d="M2 66h68"/></svg>
    <div><h3>HIGH END</h3><p>Lorem ipsum dolor sit amet,<br>consectetur adipiscing elit, sed do<br>eiusmod temporincididunt ut</p></div>
  </div>
  <div class="feature">
    <svg width="80" height="72" viewBox="0 0 80 72" fill="none" stroke="#EE7325" stroke-width="2.4"><rect x="6" y="10" width="66" height="40" rx="2"/><path d="M18 10v40M30 10v40M42 10v40M54 10v40M2 54h76M72 30h6"/><circle cx="40" cy="62" r="7"/><circle cx="56" cy="62" r="7"/></svg>
    <div><h3>CONVENIENT</h3><p>Lorem ipsum dolor sit amet,<br>consectetur adipiscing elit, sed do<br>eiusmod temporincididunt ut</p></div>
  </div>
  <div class="feature">
    <svg width="72" height="72" viewBox="0 0 72 72" fill="none" stroke="#EE7325" stroke-width="2.4"><path d="M10 34h12v30H10zM22 36l10-18c2-4 8-3 8 2v10h18c4 0 6 4 5 7l-5 22c-1 3-3 5-6 5H22"/><path d="M50 8v8M46 12h8M62 20v6M59 23h6M30 4l2 4M20 12l3 2"/></svg>
    <div><h3>VERSATILE</h3><p>Lorem ipsum dolor sit amet,<br>consectetur adipiscing elit, sed do<br>eiusmod temporincididunt ut</p></div>
  </div>
</section>

<section class="about">
  <div class="about-img" role="img" aria-label="Photo of a grey three-stall restroom trailer with blue entry steps"></div>
  <h2>About US</h2>
  <div class="copy">
    <p>Lorem ipsum dolor sit amet, consectetur adipiscing elit, sed do eiusmod tempor incididunt ut labore et dolore magna aliqua. Ut enim ad minim veniam, quis nostrud exercitation ullamco laboris nisi ut aliquip ex ea commodo consequat. Duis aute irure dolor in reprehenderit in voluptate velit esse cillum dolore eu fugiat nulla pariatur.</p>
    <p>Lorem ipsum dolor sit amet, consectetur adipiscing elit, sed do eiusmod tempor incididunt ut labore et dolore magna aliqua. Ut enim ad minim veniam, quis nostrud exercitation ullamco laboris nisi ut aliquip ex ea commodo consequat. Duis aute irure dolor in reprehenderit in voluptate velit esse cillum dolore eu fugiat nulla pariatur.</p>
  </div>
  <span class="btn orange">Learn more</span>
</section>

<section class="trailers">
  <h2 class="title" style="top:1418px">Our Luxury Trailers</h2>
  <div class="rule" style="top:1485px"></div>
  <svg class="arrow" style="left:35px;top:1719px" viewBox="0 0 64 64" fill="none" stroke="#EE7325" stroke-width="4"><circle cx="32" cy="32" r="29"/><path d="M37 20 25 32l12 12"/></svg>
  <svg class="arrow" style="left:1078px;top:1713px" viewBox="0 0 64 64" fill="none" stroke="#EE7325" stroke-width="4"><circle cx="32" cy="32" r="29"/><path d="M27 20l12 12-12 12"/></svg>
  <div class="cards">
    <div class="trailer" role="img" aria-label="Photo of a two-stall restroom trailer">
      <h4>2 Stall Trailer</h4>
      <div class="spec"><div><b>SIZE :</b> <span>144-1/2"</span></div><div><b>CONDITION :</b> <span>New</span></div></div>
      <div class="req">REQUEST A QUOTE</div>
    </div>
    <div class="trailer" role="img" aria-label="Photo of a two-stall restroom trailer">
      <h4 style="top:288px">2 Stall Trailer</h4>
      <div class="spec" style="top:333px"><div><b>SIZE :</b> <span>144-1/2"</span></div><div><b>CONDITION :</b> <span>New</span></div></div>
      <div class="req" style="top:371px">REQUEST A QUOTE</div>
    </div>
    <div class="trailer" role="img" aria-label="Photo of a two-stall restroom trailer">
      <h4 style="top:288px">2 Stall Trailer</h4>
      <div class="spec" style="top:333px"><div><b>SIZE :</b> <span>144-1/2"</span></div><div><b>CONDITION :</b> <span>New</span></div></div>
      <div class="req" style="top:371px">REQUEST A QUOTE</div>
    </div>
  </div>
</section>

<section class="events" role="img" aria-label="Faded photo of an outdoor event tent beside a restroom trailer">
  <h2 class="title" style="top:81px">Perfect for Any Event</h2>
  <div class="event" style="left:99px;top:230px"><div class="pic" role="img" aria-label="Photo of a seaside wedding setup" style="background:linear-gradient(160deg,#9fc7e6,#e9d7cf 60%,#c9a98a)"></div><span style="top:226px">WEDDING</span></div>
  <div class="event" style="left:369px;top:230px"><div class="pic" role="img" aria-label="Photo of a festive dinner event with hanging lights" style="background:linear-gradient(170deg,#3d4a3d,#6b6a55 50%,#2d2b25)"></div><span style="top:226px">EVENTS</span></div>
  <div class="event" style="left:640px;top:230px"><div class="pic" role="img" aria-label="Photo of guests enjoying an outdoor party" style="background:linear-gradient(160deg,#7da04a,#b99a6e 55%,#6f8a40)"></div><span style="top:230px">PARTIES</span></div>
  <div class="event" style="left:910px;top:230px"><div class="pic" role="img" aria-label="Photo of volunteers at an outdoor charity event" style="background:linear-gradient(160deg,#6f8f55,#d88a4a 50%,#8a8fae)"></div><span style="top:230px">CHARITY EVENTS</span></div>
</section>

<section class="pricing">
  <h2 class="title" style="top:2616px">Pricing</h2>
  <div class="rule" style="top:2681px"></div>
  <div class="price-panel"><div class="price-tabbar"></div></div>

  <div class="plan" style="left:142px">
    <h5>Basic Plan</h5><div class="sub">This is Basic Plan</div>
    <div class="amount"><small>$</small><strong>79</strong><em>/ MONTHLY</em></div>
    <ul><li>Branding<b>✓</b></li><li>20 hours of consultation<b>✓</b></li><li>15 hours if theory<b>✓</b></li><li>Parlo video call<b>✓</b></li><li>Support 24/7<b>✓</b></li></ul>
    <div class="choose">Choose Plan</div>
  </div>
  <div class="plan" style="left:454px">
    <h5>Standart Plan</h5><div class="sub">This is Standart Plan</div>
    <div class="amount"><small>$</small><strong>129</strong><em>/ MONTHLY</em></div>
    <ul><li>Branding<b>✓</b></li><li>20 hours of consultation<b>✓</b></li><li>15 hours if theory<b>✓</b></li><li>Parlo video call<b>✓</b></li><li>Support 24/7<b>✓</b></li></ul>
    <div class="choose">Choose Plan</div>
  </div>
  <div class="plan" style="left:766px">
    <div class="ribbon">Popular</div>
    <h5>Premium Plan</h5><div class="sub">This is Premium Plan</div>
    <div class="amount"><small>$</small><strong>259</strong><em>/ MONTHLY</em></div>
    <ul><li>Branding<b>✓</b></li><li>20 hours of consultation<b>✓</b></li><li>15 hours if theory<b>✓</b></li><li>Parlo video call<b>✓</b></li><li>Support 24/7<b>✓</b></li></ul>
    <div class="choose">Choose Plan</div>
  </div>
</section>

<section class="areas">
  <h2 class="title" style="top:3346px">Areas We Serve</h2>
  <div class="rule" style="top:3412px"></div>
  <div class="area" style="left:56px;top:3488px"><span class="tick"><svg width="30" height="24" viewBox="0 0 30 24"><path d="M3 12l8 8L27 3" stroke="#fff" stroke-width="4" fill="none"/></svg></span>Los Angeles County</div>
  <div class="area" style="left:484px;top:3492px"><span class="tick"><svg width="30" height="24" viewBox="0 0 30 24"><path d="M3 12l8 8L27 3" stroke="#fff" stroke-width="4" fill="none"/></svg></span>Riverside County</div>
  <div class="area" style="left:912px;top:3494px"><span class="tick"><svg width="30" height="24" viewBox="0 0 30 24"><path d="M3 12l8 8L27 3" stroke="#fff" stroke-width="4" fill="none"/></svg></span>Palm Desert</div>
  <div class="area" style="left:56px;top:3587px"><span class="tick"><svg width="30" height="24" viewBox="0 0 30 24"><path d="M3 12l8 8L27 3" stroke="#fff" stroke-width="4" fill="none"/></svg></span>Orange County</div>
  <div class="area" style="left:484px;top:3591px"><span class="tick"><svg width="30" height="24" viewBox="0 0 30 24"><path d="M3 12l8 8L27 3" stroke="#fff" stroke-width="4" fill="none"/></svg></span>San Bernardino County</div>
  <div class="area" style="left:912px;top:3593px"><span class="tick"><svg width="30" height="24" viewBox="0 0 30 24"><path d="M3 12l8 8L27 3" stroke="#fff" stroke-width="4" fill="none"/></svg></span>Santa Ana</div>
</section>

<footer class="footer">
  <div class="brand"><span class="sq"></span>Wavelet Hire</div>
  <p class="about-text">Lorem ipsum dolor sit amet, consectetur adipiscing elit, sed do eiusmod temporincididunt ut labore et dolore magna aliqua. Ut enim ad minim veniam, quis nostrud</p>

  <h6 style="left:422px">Quick Links</h6>
  <ul class="flist" style="left:422px;top:88px">
    <li><span class="fcheck"><svg width="12" height="10" viewBox="0 0 12 10"><path d="M1 5l3 3 7-7" stroke="#fff" stroke-width="2" fill="none"/></svg></span>HOME</li>
    <li><span class="fcheck"><svg width="12" height="10" viewBox="0 0 12 10"><path d="M1 5l3 3 7-7" stroke="#fff" stroke-width="2" fill="none"/></svg></span>ABOUT</li>
    <li><span class="fcheck"><svg width="12" height="10" viewBox="0 0 12 10"><path d="M1 5l3 3 7-7" stroke="#fff" stroke-width="2" fill="none"/></svg></span>TRAILERS</li>
    <li><span class="fcheck"><svg width="12" height="10" viewBox="0 0 12 10"><path d="M1 5l3 3 7-7" stroke="#fff" stroke-width="2" fill="none"/></svg></span>PRICES</li>
    <li><span class="fcheck"><svg width="12" height="10" viewBox="0 0 12 10"><path d="M1 5l3 3 7-7" stroke="#fff" stroke-width="2" fill="none"/></svg></span>CONTACT</li>
  </ul>

  <h6 style="left:657px">Contact Info</h6>
  <ul class="flist" style="left:657px;top:92px">
    <li style="height:46px"><svg width="20" height="16" viewBox="0 0 20 16"><rect width="20" height="16" rx="2" fill="#EE7325"/><path d="M2 3l8 6 8-6" stroke="#fff" stroke-width="1.6" fill="none"/></svg>info@website</li>
    <li style="height:44px"><svg width="20" height="20" viewBox="0 0 20 20"><rect width="20" height="20" rx="2" fill="#EE7325"/><path d="M6 5c0 5 4 9 9 9l1-2-2.5-1.5-1.3 1.2c-1.6-.8-2.6-1.8-3.4-3.4L10 7 8.5 4.5z" fill="#fff"/></svg>123-456-7890</li>
    <li><svg width="20" height="20" viewBox="0 0 20 20"><rect width="20" height="20" rx="2" fill="#EE7325"/><path d="M10 3a5 5 0 0 0-5 5c0 4 5 9 5 9s5-5 5-9a5 5 0 0 0-5-5z" fill="#fff"/><circle cx="10" cy="8" r="2" fill="#EE7325"/></svg>Santa Ana California</li>
  </ul>

  <h6 style="left:921px">Newsletter</h6>
  <div class="input">Email Address</div>
  <div class="signup">SIGNUP NOW</div>

  <div class="line"></div>
  <p class="copyright">Copyright 2024, Wavelet Hire. All Rights Reserved.</p>
  <div class="social"><i class="dot"></i><i class="dot"></i><i class="dot"></i></div>
</footer>

</body>
</html>
```